Trade Show Banner

Looking for a design for 36" x 90" stretched fabric display.
Commercial construction company, can include Chicago high rise buildings, blue prints, steel studs.
List of types of work should include:
Commercial office build-out
Hospital expansion
Educational and institutional
Laboratory and research
Dental and medical office
Veterinary Clinics

website brolmerconstruction.com

Target Market(s)

Architects and General Contractors

Industry/Entity Type

Commercial Construction

Colors
0054AA
0677BA
7BADD7
CADEEF
E8F1F8

Requirements
Must have
• Our logo, blueprints, chicago high rise
Should not have
• no cartoon construction logos, no houses

```html
<!DOCTYPE html>
<html lang="en">
<head>
<meta charset="utf-8">
<title>Brolmer Construction – Trade Show Banner</title>
<link href="https://fonts.googleapis.com/css2?family=Archivo:wght@700;800;900&family=Russo+One&display=swap" rel="stylesheet">
<style>
  :root{
    --page:#c4c4c4;
    --charcoal:#2b2b2b;
    --blue-deep:#0054AA;
    --blue:#0677BA;
    --blue-mid:#7BADD7;
    --blue-pale:#CADEEF;
    --blue-mist:#E8F1F8;
    --logo-blue:#1b82dc;
    --ink:#3b3b3b;
    --panel:#f1f1f1;
  }
  *{margin:0;padding:0;box-sizing:border-box}
  html,body{width:797px;height:1200px;overflow:hidden;background:var(--page)}
  .banner{position:absolute;left:178px;top:51px;width:440px;height:1097px;box-shadow:14px 12px 18px rgba(0,0,0,.35)}
  .banner-art{position:absolute;inset:0;width:100%;height:100%;display:block}
  .brand{position:absolute;left:0;right:0;top:58px;display:flex;justify-content:center;align-items:center;gap:12px}
  .brand-square{width:34px;height:34px;background:var(--logo-blue)}
  .brand-name{font-family:"Archivo",sans-serif;font-weight:900;color:var(--logo-blue);font-size:27px;line-height:1;letter-spacing:1px;text-transform:uppercase}
  .services{position:absolute;left:0;right:0;top:641px;display:grid;grid-template-columns:repeat(3,1fr);row-gap:18px;padding:0 18px}
  .service{display:flex;flex-direction:column;align-items:center;position:relative}
  .service + .service:not(:nth-child(4))::before{content:"";position:absolute;left:0;top:58px;height:30px;border-left:1.5px solid var(--blue)}
  .service-icon{width:44px;height:48px}
  .service-label{margin-top:12px;font-family:"Archivo",sans-serif;font-weight:800;font-size:11.5px;line-height:1.2;color:var(--ink);text-align:center;text-transform:uppercase}
  .contact{position:absolute;left:0;right:0;top:874px;text-align:center}
  .contact-web{font-family:"Archivo",sans-serif;font-weight:800;font-size:13.5px;color:var(--ink);text-transform:uppercase}
  .contact-web span{color:var(--blue-deep)}
  .contact-phone{font-family:"Russo One",sans-serif;font-size:33px;color:var(--blue);letter-spacing:.5px;line-height:1.2}
</style>
</head>
<body>
<main class="banner">
  <svg class="banner-art" viewBox="0 0 377 940" preserveAspectRatio="none">
    <defs>
      <linearGradient id="skyline" x1="0" y1="0" x2="0" y2="1">
        <stop offset="0" stop-color="#3f8fd0"/>
        <stop offset=".35" stop-color="#b9d3e6"/>
        <stop offset=".5" stop-color="#d9c9bf"/>
        <stop offset=".62" stop-color="#5a7089"/>
        <stop offset="1" stop-color="#3a4450"/>
      </linearGradient>
      <linearGradient id="blueprint" x1="0" y1="0" x2="1" y2="1">
        <stop offset="0" stop-color="#2a7fd0"/>
        <stop offset="1" stop-color="#0b5fb8"/>
      </linearGradient>
    </defs>
    <rect class="city-photo" role="img" aria-label="Aerial photo of the Chicago high-rise skyline at sunset along the lake" x="0" y="0" width="377" height="700" fill="url(#skyline)"/>
    <polygon class="blueprint-art" role="img" aria-label="Blue architectural floor plan blueprint" points="377,345 130,485 377,600" fill="url(#blueprint)"/>
    <polygon class="header-band" points="0,0 377,0 377,125 188,232 0,125" fill="var(--charcoal)"/>
    <polygon class="footer-band" points="0,775 188,885 377,775 377,940 0,940" fill="var(--blue)"/>
    <polygon points="0,860 188,940 0,940" fill="#1266b8"/>
    <polygon points="377,860 188,940 377,940" fill="#1266b8"/>
    <polygon points="60,940 188,885 316,940" fill="var(--blue-deep)"/>
    <polygon class="info-panel" points="188,450 377,555 377,775 188,885 0,775 0,555" fill="var(--panel)"/>
  </svg>

  <div class="brand">
    <div class="brand-square"></div>
    <div class="brand-name">Brolmer<br>Construction</div>
  </div>

  <section class="services">
    <div class="service">
      <svg class="service-icon" viewBox="0 0 44 48"><polygon points="22,1 42,12.5 42,35.5 22,47 2,35.5 2,12.5" fill="var(--blue)"/><path d="M15 34V15h10v19M25 22h5v12M13 34h19M18 19h4M18 24h4M18 29h4" fill="none" stroke="#fff" stroke-width="1.4"/></svg>
      <div class="service-label">Commercial<br>Office Build-Out</div>
    </div>
    <div class="service">
      <svg class="service-icon" viewBox="0 0 44 48"><polygon points="22,1 42,12.5 42,35.5 22,47 2,35.5 2,12.5" fill="var(--blue)"/><path d="M13 34V20h18v14M17 20v-5h10v5M12 34h20M22 16v3M20.5 17.5h3M17 24h3M24 24h3M20 34v-5h4v5" fill="none" stroke="#fff" stroke-width="1.4"/></svg>
      <div class="service-label">Hospital<br>Expansion</div>
    </div>
    <div class="service">
      <svg class="service-icon" viewBox="0 0 44 48"><polygon points="22,1 42,12.5 42,35.5 22,47 2,35.5 2,12.5" fill="var(--blue)"/><path d="M13 34V22l9-6 9 6v12M12 34h20M17 25h3M24 25h3M17 29h3M24 29h3M22 16v-4h4" fill="none" stroke="#fff" stroke-width="1.4"/></svg>
      <div class="service-label">Educational<br>&amp; Institutional</div>
    </div>
    <div class="service">
      <svg class="service-icon" viewBox="0 0 44 48"><polygon points="22,1 42,12.5 42,35.5 22,47 2,35.5 2,12.5" fill="var(--blue)"/><path d="M12 34V18h20v16M11 34h22M12 22h20M15 26h3M20.5 26h3M26 26h3M15 30h3M26 30h3" fill="none" stroke="#fff" stroke-width="1.4"/></svg>
      <div class="service-label">Laboratory<br>&amp; Research</div>
    </div>
    <div class="service">
      <svg class="service-icon" viewBox="0 0 44 48"><polygon points="22,1 42,12.5 42,35.5 22,47 2,35.5 2,12.5" fill="var(--blue)"/><path d="M14 34V18l8-4 8 4v16M13 34h18M22 19v5M19.5 21.5h5M18 28h8M20 34v-3h4v3" fill="none" stroke="#fff" stroke-width="1.4"/></svg>
      <div class="service-label">Dental &amp;<br>Medical Office</div>
    </div>
    <div class="service">
      <svg class="service-icon" viewBox="0 0 44 48"><polygon points="22,1 42,12.5 42,35.5 22,47 2,35.5 2,12.5" fill="var(--blue)"/><path d="M12 34V20h20v14M11 34h22M12 16h20v4H12zM16 24h4v4h-4zM24 24h4v4h-4z" fill="none" stroke="#fff" stroke-width="1.4"/></svg>
      <div class="service-label">Veterinary<br>Clinics</div>
    </div>
  </section>

  <div class="contact">
    <p class="contact-web">www.<span>brolmerconstruction</span>.com</p>
    <p class="contact-phone">(312) 555-0148</p>
  </div>
</main>
</body>
</html>
```